Letterhead & Email Signature Design

Kindly assist redesign this letterhead as well as the Email signature. I have uploaded the current designs that needs some new look

```html
<!DOCTYPE html>
<html lang="en">
<head>
<meta charset="utf-8">
<title>Tladi Ncube Inc. Stationery</title>
<link href="https://fonts.googleapis.com/css2?family=Arimo:wght@400&family=Mulish:wght@400;700&display=swap" rel="stylesheet">
<style>
  :root {
    --backdrop: #cfd0d2;
    --paper: #f0f0f1;
    --ink: #555557;
    --ink-strong: #444446;
    --brand: #626263;
    --rule: #7a7a7c;
  }
  * { margin: 0; padding: 0; box-sizing: border-box; }
  html, body { width: 1200px; height: 968px; overflow: hidden; background: var(--backdrop); }
  body { position: relative; font-family: "Mulish", sans-serif; color: var(--ink); }
  .sheet { position: absolute; background: var(--paper); border-bottom: 5px solid var(--brand); }
  .abs { position: absolute; }
  .brand { display: flex; align-items: center; gap: 7px; }
  .brand-dot { border-radius: 50%; background: var(--brand); flex: none; }
  .brand-name { font-family: "Mulish", sans-serif; font-weight: 400; color: var(--ink-strong); white-space: nowrap; }
  .divider { position: absolute; width: 1px; background: var(--rule); }
  .firm { font-weight: 700; color: var(--ink-strong); }
  .contact { font-size: 8.4px; line-height: 10.3px; }
  .contact-list { list-style: none; font-size: 8.4px; line-height: 10.3px; }
  .contact-list li { display: flex; align-items: center; gap: 4px; }
  .contact-list svg { width: 6px; height: 6px; fill: var(--ink); flex: none; }
  .person { font-weight: 700; color: var(--ink-strong); }
  .role { font-size: 8.5px; }

  /* letterhead */
  .letterhead { left: 90px; top: 74px; width: 573px; height: 805px; }
  .letterhead .greeting { left: 42px; top: 274px; font-family: "Arimo", sans-serif; font-size: 14.5px; color: var(--ink); }
  .letter-body { left: 42px; top: 316px; width: 489px; font-family: "Arimo", sans-serif; font-size: 8.3px; line-height: 12.3px; text-align: justify; color: var(--ink); }
  .letter-body p { margin-bottom: 12.4px; }
  .sign-off { left: 42px; top: 586px; font-family: "Arimo", sans-serif; font-size: 8.3px; }
  .signature { left: 38px; top: 610px; width: 168px; height: 52px; background: linear-gradient(90deg, #e4e4e6, #dadadc); border-radius: 3px; }
  .footer-rule { left: 42px; top: 742px; width: 489px; height: 1px; background: var(--rule); }
  .footer { top: 753px; font-size: 8.4px; line-height: 10.3px; }
  .footer b { font-weight: 700; color: var(--ink-strong); }

  /* business cards */
  .card-tall { left: 694px; top: 297px; width: 177px; height: 290px; }
  .card-wide { left: 694px; top: 612px; width: 404px; height: 154px; }
  .card-strip { left: 694px; top: 790px; width: 404px; height: 89px; }
</style>
</head>
<body>
<svg width="0" height="0" style="position:absolute" aria-hidden="true">
  <symbol id="i-phone" viewBox="0 0 10 10"><path d="M2 0.5l2 2-1 1.3c.7 1.4 1.8 2.5 3.2 3.2l1.3-1 2 2-1.3 1.5C4.5 9.6.4 5.5.5 1.8z"/></symbol>
  <symbol id="i-fax" viewBox="0 0 10 10"><rect x="2.5" y="0.5" width="5" height="3"/><rect x="0.5" y="3.5" width="9" height="4.5" rx="1"/><rect x="2.5" y="7" width="5" height="2.5"/></symbol>
  <symbol id="i-mail" viewBox="0 0 10 10"><path d="M0.5 2h9v6h-9z M0.5 2l4.5 3.5 4.5-3.5" /></symbol>
  <symbol id="i-globe" viewBox="0 0 10 10"><circle cx="5" cy="5" r="4.5"/><path d="M3 3.5c1 .3 1.5 1 1 2.2S5.5 7 6.5 6.5 7 4 5.8 3.2z" fill="#f0f0f1"/></symbol>
</svg>

<!-- Letterhead -->
<section class="sheet letterhead">
  <div class="abs brand" style="left:42px; top:56px;">
    <span class="brand-dot" style="width:32px;height:32px;"></span>
    <span class="brand-name" style="font-size:14px;">Tladi Ncube Inc.</span>
  </div>
  <div class="divider" style="left:318px; top:42px; height:75px;"></div>
  <div class="abs contact" style="left:336px; top:41px;">
    <div class="firm">TLADI NCUBE INC.</div>
    <div>Acacia Court, First Floor, Block C</div>
    <div>57 Marula Avenue, Lynnwood, 0040</div>
    <ul class="contact-list" style="margin-top:7px;">
      <li><svg><use href="#i-phone"/></svg>012 345 6780</li>
      <li><svg><use href="#i-fax"/></svg>012 345 6799</li>
      <li><svg><use href="#i-mail"/></svg>info@tladincube.co.za</li>
      <li><svg><use href="#i-globe"/></svg>tladincube.co.za</li>
    </ul>
  </div>

  <p class="abs greeting">Dear Mr. Jacobs,</p>
  <div class="abs letter-body">
    <p>Lorem ipsum dolor sit amet, consectetur adipiscing elit. Donec orci purus, luctus vitae dignissim eu, iaculis sed purus. Vivamus faucibus, ipsum nec aliquet viverra, leo mauris condimentum ligula, sit amet sagittis enim ligula quis arcu. Nam egestas tortor id nisi porttitor mattis. In tortor ante, ultricies in suscipit a, tempus non massa. Vivamus et auctor mi. Fusce vel massa nulla. Phasellus nec eros mauris, et scelerisque orci.</p>
    <p>Donec malesuada orci vitae nulla accumsan porta a id massa. Quisque accumsan iaculis magna sit amet fringilla. Maecenas consequat, magna eget tincidunt semper, odio nibh rutrum mi, id feugiat ante nisi eu risus. Vestibulum nunc orci, rhoncus a placerat in, ultricies in mi. Cras mattis varius eros, vel fringilla nisi suscipit eget. Quisque scelerisque sagittis nulla at porttitor.</p>
    <p>Sed id augue vitae urna euismod commodo aliquet a quam. Pellentesque arcu velit, cursus et malesuada ut, consequat et diam. Nullam erat sem, rhoncus id ullamcorper vitae, rhoncus et arcu. In ultricies ultricies nulla, ut rutrum nisi iaculis at. Donec eu magna a metus ornare faucibus. Fusce aliquet faucibus ultricies. Morbi semper, est id tincidunt gravida, sem arcu adipiscing lacus, ac bibendum nulla leo eu purus. Quisque nec diam sed risus consectetur a ccumsan quis quis nibh. Vestibulum id purus lorem.</p>
    <p>It is a long established fact that a reader will be distracted by the readable content of a page when looking at its layout. The point of using Lorem Ipsum is that it has a more-or-less normal distribution of letters, as opposed to using 'Content here, content here', making it look like readable English. Many desktop publishing packages</p>
    <p>ada ut, consequat et diam. Nullam erat sem, rhoncus id ullamcorper vitae, rhoncus et arcu. In ultricies ultricies nulla, ut rutrum nisi iaculis at. Donec eu magna a metus ornare faucibus. Fusce aliquet faucibus ultricies. Morbi semper,</p>
  </div>
  <p class="abs sign-off">Sincerely,</p>
  <div class="abs signature" role="img" aria-label="Handwritten signature of the sender"></div>

  <div class="abs footer-rule"></div>
  <div class="abs footer" style="left:41px;">
    <div><b>DIRECTORS:</b> L T Dlamini B. PROC LLB (Hons) | N Ncube (LLB)</div>
    <div><b>CONSULTANT</b>: PK Ncube</div>
  </div>
  <div class="abs footer" style="right:42px; text-align:right;">
    <div><b>ATTORNEYS | CONVEYANCERS | NOTARIES</b></div>
    <div>Reg. No: 2011/004318/21</div>
  </div>
</section>

<!-- Vertical business card -->
<section class="sheet card-tall">
  <div class="abs brand" style="left:22px; top:58px;">
    <span class="brand-dot" style="width:24px;height:24px;"></span>
    <span class="brand-name" style="font-size:11px;">Tladi Ncube Inc.</span>
  </div>
  <div class="abs" style="left:22px; top:137px;">
    <div class="person" style="font-size:12.3px;">LERATO DLAMINI</div>
    <div class="role">Director</div>
  </div>
  <div class="abs contact" style="left:23px; top:176px;">
    <div class="firm">TLADI NCUBE INC.</div>
    <div>Acacia Court</div>
    <div>First Floor, Block C</div>
    <div>57 Marula Avenue,</div>
    <div>Lynnwood, 0040</div>
    <ul class="contact-list" style="margin-top:11px;">
      <li><svg><use href="#i-phone"/></svg>+27 12 345 6780</li>
      <li><svg><use href="#i-mail"/></svg>lerato@tladincube.co.za</li>
      <li><svg><use href="#i-globe"/></svg>www.tladincubeinc.co.za</li>
    </ul>
  </div>
</section>

<!-- Wide business card -->
<section class="sheet card-wide">
  <div class="abs brand" style="left:16px; top:66px;">
    <span class="brand-dot" style="width:22px;height:22px;"></span>
    <span class="brand-name" style="font-size:10px;">Tladi Ncube Inc.</span>
  </div>
  <div class="divider" style="left:156px; top:34px; height:90px;"></div>
  <div class="abs" style="left:176px; top:29px;">
    <div class="person" style="font-size:12.3px;">LERATO DLAMINI</div>
    <div class="role">Director</div>
  </div>
  <div class="abs contact" style="left:177px; top:64px;">
    <div class="firm">TLADI NCUBE INC.</div>
    <div>Acacia Court, First Floor, Block C</div>
    <div>57 Marula Avenue, Lynnwood, 0040</div>
    <ul class="contact-list" style="margin-top:6px;">
      <li><svg><use href="#i-phone"/></svg>+27 12 345 6780</li>
      <li><svg><use href="#i-mail"/></svg>lerato@tladincube.co.za</li>
      <li><svg><use href="#i-globe"/></svg>www.tladincubeinc.co.za</li>
    </ul>
  </div>
</section>

<!-- Strip business card -->
<section class="sheet card-strip">
  <div class="abs brand" style="left:12px; top:36px; flex-direction:column; align-items:flex-start; gap:3px;">
    <span class="brand-dot" style="width:14px;height:14px;"></span>
    <span class="brand-name" style="font-size:8px;">Tladi Ncube Inc.</span>
  </div>
  <div class="divider" style="left:101px; top:17px; height:56px;"></div>
  <div class="abs" style="left:119px; top:14px;">
    <div class="person" style="font-size:10px;">LERATO DLAMINI</div>
    <div class="role" style="font-size:8.2px;">Director</div>
    <ul class="contact-list" style="margin-top:3px;">
      <li><svg><use href="#i-phone"/></svg>+27 12 345 6780</li>
      <li><svg><use href="#i-mail"/></svg>lerato@tladincube.co.za</li>
      <li><svg><use href="#i-globe"/></svg>www.tladincubeinc.co.za</li>
    </ul>
  </div>
  <div class="divider" style="left:269px; top:17px; height:56px;"></div>
  <div class="abs contact" style="left:286px; top:18px;">
    <div class="firm">TLADI NCUBE INC.</div>
    <div>Acacia Court</div>
    <div>First Floor, Block C</div>
    <div>57 Marula Avenue,</div>
    <div>Lynnwood, 0040</div>
  </div>
</section>
</body>
</html>
```